Northgate Roofing Works Inc Business cards

Commercial and Residential Roofing contractor needs design logo and card design. Can be single or double sided but must incorporate:
Persons Name:
Persons Title:
Mailing Address: PO Box 3719
Physical Address: 58 Fenwick Lane
Millbrook, Ma. 01623
800-316-5842
508-712-5842
Fax: 508-712-5867
Cell: Person Cell number
email address
Website: WWW.northgateroofworks.com

Target Market(s)

Residential home owners and commercial building owners

Industry/Entity Type

Roofing

Contact Information for Business Card

Persons Name:
Persons Title:
Millbrook, Ma. 01623
800-316-5842
508-712-5842
Fax: 508-712-5867
Cell: Person Cell number
email address

Logo Text

Large enough to service small enough to care

Font styles to use
Serif

Colors
0355a3

Requirements
Must have
• Commercial and Residential Roofing contractor needs design logo and card design. Can be single or double sided but must incorporate:
• Persons Name:
• Persons Title:
• Mailing Address: PO Box 3719
• Physical Address: 58 Fenwick Lane
• Millbrook, Ma. 01623
• 800-316-5842
• 508-712-5842
• Fax: 508-712-5867
• Cell: Person Cell number
• email address
• Website: WWW.northgateroofworks.com
Nice to have
• ..
Should not have
• I'm looking for something different. I have had the same card for 23 years. I attached what both sides of my present card looks like.

```html
<!DOCTYPE html>
<html lang="en">
<head>
<meta charset="utf-8">
<title>Northgate Roofing Works Inc – Business Cards</title>
<link rel="stylesheet" href="https://fonts.googleapis.com/css2?family=Open+Sans:wght@400;600&display=swap">
<style>
  :root {
    --backdrop: #000000;
    --card: #343539;
    --card-deep: #2e2f33;
    --text-light: #d9d9d9;
    --text-muted: #c4c4c4;
    --brand-blue: #1f3a9e;
    --rule: #8a8b8e;
    --divider: #45464a;
  }
  * { margin: 0; padding: 0; box-sizing: border-box; }
  html, body {
    width: 1200px; height: 900px; overflow: hidden;
    background: var(--backdrop);
    font-family: "Open Sans", sans-serif;
  }
  .stage { position: relative; width: 1200px; height: 900px; }
  .card {
    position: absolute; top: 271px; width: 457px; height: 281px;
    border-radius: 14px;
    background: linear-gradient(160deg, var(--card) 0%, var(--card-deep) 100%);
    overflow: hidden;
  }
  .card--front { left: 137px; }
  .card--back { left: 626px; }

  /* front */
  .brand-name--front {
    position: absolute; left: 40px; top: 118px; width: 170px;
    color: var(--brand-blue); font-weight: 600; font-size: 19px; line-height: 1.2;
  }
  .card__divider {
    position: absolute; left: 222px; top: 68px; width: 1px; height: 196px;
    background: var(--divider);
  }
  .contact { position: absolute; left: 249px; top: 47px; color: var(--text-light); }
  .contact__name { font-size: 16.5px; font-weight: 600; line-height: 1.2; }
  .contact__title { font-size: 12px; line-height: 1.3; color: var(--text-muted); }
  .contact__address { margin-top: 19px; font-size: 12.5px; line-height: 14px; color: var(--text-muted); }
  .contact__list { list-style: none; margin-top: 14px; font-size: 12.5px; color: var(--text-muted); }
  .contact__list li { display: flex; align-items: center; height: 19px; }
  .contact__list svg { width: 10px; height: 10px; margin-right: 7px; fill: var(--text-muted); }

  /* back */
  .brand-name--back {
    position: absolute; left: 0; right: 0; top: 140px; text-align: center;
    color: var(--brand-blue); font-weight: 400; font-size: 25px;
  }
  .web-line {
    position: absolute; left: 0; right: 0; top: 234px;
    display: flex; align-items: center;
  }
  .web-line__rule { flex: 1; height: 1px; background: var(--rule); }
  .web-line__address {
    padding: 0 10px; color: var(--text-muted); font-size: 12.5px; line-height: 18px;
    white-space: nowrap;
  }
</style>
</head>
<body>
<main class="stage">
  <section class="card card--front">
    <div class="brand-name brand-name--front">Northgate Roofing Works Inc</div>
    <div class="card__divider"></div>
    <div class="contact">
      <div class="contact__name">Daniel Hartwell</div>
      <div class="contact__title">Managing Director</div>
      <div class="contact__address">PO Box 3719 58 Fenwick Lane<br>Millbrook, Ma. 01623</div>
      <ul class="contact__list">
        <li><svg viewBox="0 0 10 10"><path d="M2 0.5l1.6 2-0.9 1.1c0.6 1.3 1.5 2.2 2.7 2.8l1.1-0.9 2 1.6-1 1.8C4.2 8.6 1.2 5.7 0.5 1.6z"/></svg>800-316-5842</li>
        <li><svg viewBox="0 0 10 10"><path d="M2 0.5l1.6 2-0.9 1.1c0.6 1.3 1.5 2.2 2.7 2.8l1.1-0.9 2 1.6-1 1.8C4.2 8.6 1.2 5.7 0.5 1.6z"/></svg>508-712-5842</li>
        <li><svg viewBox="0 0 10 10"><path d="M2 0h5v3H2zM0 3.5h10V9H0zM2 6h6v1H2z"/></svg>508-712-5867</li>
        <li><svg viewBox="0 0 10 10"><path d="M2.5 0h5a1 1 0 0 1 1 1v8a1 1 0 0 1-1 1h-5a1 1 0 0 1-1-1V1a1 1 0 0 1 1-1zM2.7 1.2v6.6h4.6V1.2z"/></svg>124-587-306</li>
        <li><svg viewBox="0 0 10 10"><path d="M0 2h10v1L5 6 0 3zM0 4l5 3 5-3v4H0z"/></svg>info@northgateroofworks.com</li>
      </ul>
    </div>
  </section>

  <section class="card card--back">
    <div class="brand-name brand-name--back">Northgate Roofing Works Inc</div>
    <div class="web-line">
      <span class="web-line__rule"></span>
      <span class="web-line__address">WWW.northgateroofworks.com</span>
      <span class="web-line__rule"></span>
    </div>
  </section>
</main>
</body>
</html>
```